Movie poster for short film: TINDERLOCK

We need a creative, artistic, stylized poster design for our short film TINDERLOCK. We would like to see designs with graphics and bold colors more than photographs. The photographs we are posting are more for reference- you do not have to use them in the poster! We are looking for something clean and simple. The film is a drama so please don't make it funny. The mood of the film is thoughtful and introspective. Name of film should be in all caps. Things to include in the poster:
Name of film: TINDERLOCK
Lantern Hollow Productions
Starring Marisa Kovalenko

Here is a brief plot synopsis: TINDERLOCK follows one night in the life of a rebellious young woman who breaks into a diner after hours with a can of spray paint. Her intentions change after she ends up discovering what's left of a love story.

The movie is somewhat experimental, set to music for part of it with no dialog. The whole movie takes place in an old fashioned diner.

Target Market(s)

Film festival attendees between the ages of 20-50

Industry/Entity Type

Movie

Font styles to use
Sans Serif

Requirements
Must have
• See project description above- also the film is somewhat dark in nature so please don't make it too 'happy' looking.

```html
<!DOCTYPE html>
<html lang="en">
<head>
<meta charset="utf-8">
<title>TINDERLOCK — Poster</title>
<link rel="stylesheet" href="https://fonts.googleapis.com/css2?family=Open+Sans:wdth,wght@75..100,600..800&display=swap">
<style>
  :root {
    --ink: #000000;
    --umber: #2a261d;
    --magenta: #e6217f;
    --paper: #ffffff;
  }
  html, body {
    margin: 0;
    padding: 0;
    width: 900px;
    height: 1200px;
    overflow: hidden;
    background: var(--ink);
  }
  .poster {
    position: relative;
    width: 900px;
    height: 1200px;
    background: var(--ink);
    overflow: hidden;
    font-family: "Open Sans", sans-serif;
  }
  .title {
    position: absolute;
    left: 0;
    top: 74px;
    width: 900px;
    margin: 0;
    text-align: center;
    font-family: "Open Sans", sans-serif;
    font-weight: 700;
    font-stretch: 75%;
    font-size: 150px;
    line-height: 1;
    letter-spacing: 0;
    white-space: nowrap;
    color: var(--umber);
    text-shadow: 4px 4px 0 var(--magenta);
  }
  .orb {
    position: absolute;
    left: 0;
    top: 0;
    width: 900px;
    height: 1200px;
  }
  .orb .orb-ring { fill: var(--umber); }
  .orb .orb-core { fill: var(--magenta); }
  .credits {
    position: absolute;
    left: 0;
    top: 1037px;
    margin: 0;
    padding: 0;
    list-style: none;
  }
  .credit {
    display: block;
    box-sizing: border-box;
    height: 41px;
    margin-bottom: 3px;
    background: var(--umber);
    color: var(--paper);
    font-weight: 700;
    font-size: 25px;
    line-height: 41px;
    letter-spacing: -0.4px;
    white-space: nowrap;
  }
  .credit--studio { margin-left: 75px; width: 545px; padding-left: 12px; }
  .credit--star { margin-left: 63px; width: 409px; padding-left: 24px; }
</style>
</head>
<body>
  <main class="poster">
    <h1 class="title">TINDERLOCK</h1>

    <svg class="orb" viewBox="0 0 900 1200" aria-hidden="true">
      <ellipse class="orb-ring" cx="450" cy="615" rx="361" ry="323"/>
      <ellipse class="orb-core" cx="450" cy="616" rx="324" ry="292"/>
    </svg>

    <ul class="credits">
      <li class="credit credit--studio">Lantern Hollow Productions</li>
      <li class="credit credit--star">Starring Marisa Kovalenko</li>
    </ul>
  </main>
</body>
</html>
```